New Business Card Design Project

I have a logo I would like to use on the business card. I want something that will stand out and that will be remembered.

Target Market(s)

People who collect gems, minerals and crystals.

Contact Information for Business Card

email - tkstonefalcon@mailbrook.net
phone # 617-203-4958

Font styles to use
Serif
Sans Serif
Decorative

Colors

Designer to choose colors to be used in the design.

Requirements
Must have
• The logo...two to choose from.
Nice to have
• An eye catching and memorable way to draw in people who collect gems minerals and crystals.

```html
<!DOCTYPE html>
<html lang="en">
<head>
<meta charset="utf-8">
<title>Stone Falcon — Business Card</title>
<link href="https://fonts.googleapis.com/css2?family=Alfa+Slab+One&family=Oswald:wght@500&family=Noto+Serif:wght@400&display=swap" rel="stylesheet">
<style>
  :root {
    --canvas: #e6e6e6;
    --royal: #0a07c4;
    --ink: #000000;
    --paper: #f2f0f0;
    --paper-shade: #dedcdc;
    --white: #ffffff;
  }
  * { margin: 0; padding: 0; box-sizing: border-box; }
  html, body { width: 1200px; height: 1200px; overflow: hidden; background: var(--canvas); }
  .canvas { position: relative; width: 1200px; height: 1200px; }

  .card { position: absolute; left: 262px; width: 686px; height: 392px; border-radius: 22px; overflow: hidden; }
  .card--front { top: 165px; background: linear-gradient(135deg, var(--paper), var(--paper-shade) 60%, var(--paper)); }
  .card--back { top: 653px; background: var(--ink); }

  .front-art { position: absolute; inset: 0; width: 686px; height: 392px; }

  .wordmark { font-family: "Alfa Slab One", serif; font-weight: 400; text-transform: uppercase; line-height: 1; }
  .wordmark span { display: block; }

  .front-logo { position: absolute; left: 352px; top: 222px; width: 300px; text-align: center; }
  .front-logo .wordmark { color: var(--ink); font-size: 48px; letter-spacing: 2px; }
  .front-logo .wordmark span + span { margin-top: 4px; letter-spacing: 7px; }

  .tagline { display: flex; align-items: center; gap: 4px; font-family: "Oswald", sans-serif; font-weight: 500; color: var(--royal); letter-spacing: 2px; text-transform: uppercase; white-space: nowrap; }
  .tagline::before, .tagline::after { content: ""; flex: 1; height: 3px; background: var(--royal); }
  .front-logo .tagline { margin-top: 8px; font-size: 11px; }

  .mascot-mark { position: absolute; left: 266px; top: 38px; width: 154px; height: 156px; border-radius: 50% 50% 18px 18px; background: linear-gradient(180deg, #f4f4f4, #cfcfcf); }

  .back-logo { position: absolute; left: 0; right: 0; top: 200px; margin: 0 auto; width: 232px; text-align: center; }
  .back-logo .rule { height: 2px; background: var(--white); margin-bottom: 10px; }
  .back-logo .wordmark { color: var(--white); font-size: 36px; letter-spacing: 1px; }
  .back-logo .wordmark span + span { margin-top: 4px; letter-spacing: 5px; }
  .back-logo .tagline { margin-top: 5px; font-size: 8px; letter-spacing: 1px; }

  .contact-band { position: absolute; left: 0; right: 0; top: 333px; height: 33px; background: var(--royal);
    display: flex; align-items: center; justify-content: center; gap: 12px;
    font-family: "Noto Serif", serif; font-size: 19px; color: var(--white); white-space: nowrap; }
  .contact-item { display: flex; align-items: center; gap: 6px; }
  .contact-item svg { width: 16px; height: 16px; fill: var(--white); }
</style>
</head>
<body>
<div class="canvas">

  <section class="card card--front">
    <svg class="front-art" viewBox="0 0 686 392">
      <defs>
        <linearGradient id="crystalTone" x1="0" y1="0" x2="1" y2="1">
          <stop offset="0" stop-color="#f5f3f3"/>
          <stop offset="1" stop-color="#e2e0e0"/>
        </linearGradient>
        <linearGradient id="mascotTone" x1="0" y1="0" x2="0" y2="1">
          <stop offset="0" stop-color="#1a1a1a"/>
          <stop offset="1" stop-color="#000"/>
        </linearGradient>
      </defs>
      <rect class="texture" x="300" y="0" width="386" height="392" fill="url(#crystalTone)" role="img" aria-label="Faint faceted crystal texture background"/>
      <path class="brand-panel" d="M0 0 H303 C280 30 250 60 240 90 L95 380 L95 392 H0 Z" fill="var(--royal)"/>
      <path class="base-strip" d="M0 380 C200 372 400 375 686 386 V392 H0 Z" fill="var(--ink)"/>
      <rect class="mascot" x="20" y="14" width="300" height="362" rx="60" fill="url(#mascotTone)" opacity="0.92" role="img" aria-label="Mascot illustration: masked figure holding crystals with crossed pickaxes"/>
    </svg>
    <div class="front-logo">
      <div class="wordmark"><span>Stone</span><span>Falcon</span></div>
      <div class="tagline">Gems · Minerals · Crystals</div>
    </div>
  </section>

  <section class="card card--back">
    <div class="mascot-mark" role="img" aria-label="Mascot illustration in white: masked figure holding crystals with crossed pickaxes"></div>
    <div class="back-logo">
      <div class="rule"></div>
      <div class="wordmark"><span>Stone</span><span>Falcon</span></div>
      <div class="tagline">Gems · Minerals · Crystals</div>
    </div>
    <div class="contact-band">
      <span class="contact-item">
        <svg viewBox="0 0 16 16"><circle cx="8" cy="4.5" r="3.5"/><path d="M1 16c0-4 3-6.5 7-6.5s7 2.5 7 6.5z"/></svg>
        TK Marlowe
      </span>
      <span class="contact-item">
        <svg viewBox="0 0 16 16"><path d="M3.5 1l3 3-1.8 2.2c1 2 2.6 3.6 4.6 4.6L11.5 9l3 3-2 3C6.5 15 1 9.5 1 3.5z"/></svg>
        617-203-4958
      </span>
      <span class="contact-item">
        <svg viewBox="0 0 16 16"><path d="M1 4h14v9H1z"/><path d="M1 4l7 5 7-5" fill="none" stroke="#0a07c4" stroke-width="1.4"/></svg>
        tkstonefalcon@mailbrook.net
      </span>
    </div>
  </section>

</div>
</body>
</html>
```